Design a business card
Business name: Kestrel Yield Consulting
Improving Business Profitibility

- An Overview of the Business & Service:

Business Performance Consulting

- The Target Market: Small to medium-sized business

- Design Specifics:
White card, blue ink, moon eclipse

No Logo

Target Market(s)

Small to medium-sized business

Font styles to use
Sans Serif

```html
<!DOCTYPE html>
<html lang="en">
<head>
<meta charset="utf-8">
<title>Kestrel Yield Consulting – Business Card</title>
<link rel="stylesheet" href="https://fonts.googleapis.com/css2?family=Open+Sans:wght@400;700&family=Poppins:wght@500&display=swap">
<style>
  :root {
    --ink-blue: #0a5fcc;
    --stripe-cyan: #19b7e8;
    --stripe-mid: #1497c9;
    --stripe-teal: #0a7f9c;
    --text-dark: #2b2b2b;
    --card-white: #ffffff;
    --page-bg: #eceae7;
  }
  * { margin: 0; padding: 0; box-sizing: border-box; }
  html, body { width: 1200px; height: 1200px; overflow: hidden; }
  body { background: var(--page-bg); position: relative; font-family: "Open Sans", sans-serif; }

  .card {
    position: absolute;
    width: 707px; height: 403px;
    background: var(--card-white);
    overflow: hidden;
  }
  .card--front { left: 180px; top: 222px; }
  .card--back  { left: 313px; top: 675px; }

  .accent-stripe { position: absolute; top: 0; width: 5px; }
  .accent-stripe--1 { left: 0;  height: 90px; background: var(--stripe-cyan); }
  .accent-stripe--2 { left: 10px; height: 70px; background: var(--stripe-mid); }
  .accent-stripe--3 { left: 20px; height: 45px; background: var(--stripe-teal); }

  .holder { position: absolute; left: 26px; top: 44px; color: var(--text-dark); }
  .holder__name { font-family: "Poppins", sans-serif; font-weight: 500; font-size: 29px; line-height: 1; letter-spacing: -0.3px; }
  .holder__title { font-size: 17px; margin-top: 6px; }

  .brand {
    position: absolute;
    display: flex; align-items: center; gap: 12px;
    color: var(--ink-blue);
  }
  .brand__dot { flex: none; border-radius: 50%; background: var(--ink-blue); }
  .brand__name { font-weight: 700; line-height: 1.05; text-transform: uppercase; }
  .brand__name span { display: block; }
  .card--front .brand { right: 28px; top: 34px; }
  .card--front .brand__dot { width: 22px; height: 22px; }
  .card--front .brand__name { font-size: 30px; }
  .card--back .brand { left: 0; right: 0; top: 150px; justify-content: center; gap: 16px; }
  .card--back .brand__dot { width: 28px; height: 28px; }
  .card--back .brand__name { font-size: 40px; }

  .contacts {
    position: absolute; left: 26px; top: 272px;
    display: grid; grid-template-columns: 220px auto; row-gap: 6px;
    color: var(--ink-blue); font-size: 17px;
  }
  .contact { display: flex; align-items: center; gap: 10px; height: 26px; }
  .icon { width: 26px; height: 26px; flex: none; }

  .band {
    position: absolute; left: 0; right: 0; bottom: 0; height: 49px;
    background: var(--ink-blue); color: var(--card-white);
    display: flex; align-items: center; font-size: 17px;
  }
  .card--front .band { padding-left: 26px; gap: 6px; }
  .card--back .band { justify-content: center; font-size: 18px; }
</style>
</head>
<body>

<section class="card card--front" aria-label="Card front">
  <div class="accent-stripe accent-stripe--1"></div>
  <div class="accent-stripe accent-stripe--2"></div>
  <div class="accent-stripe accent-stripe--3"></div>

  <div class="holder">
    <p class="holder__name">Desmond R Hale</p>
    <p class="holder__title">Director</p>
  </div>

  <div class="brand">
    <span class="brand__dot"></span>
    <p class="brand__name"><span>Kestrel Yield</span><span>Consulting</span></p>
  </div>

  <div class="contacts">
    <div class="contact">
      <svg class="icon" viewBox="0 0 26 26" fill="none" stroke="currentColor" stroke-width="1.6"><circle cx="13" cy="13" r="11.5"/><path d="M7.5 11c0-2 2.5-3 5.5-3s5.5 1 5.5 3l-1.8.8-1-1.6h-5.4l-1 1.6z M9 12.5h8l1 5H8z" fill="currentColor" stroke="none"/></svg>
      <span>Tel: 00 987654321</span>
    </div>
    <div class="contact">
      <svg class="icon" viewBox="0 0 26 26" fill="none" stroke="currentColor" stroke-width="1.6"><circle cx="13" cy="13" r="11.5"/><rect x="8" y="9" width="10" height="5" fill="currentColor" stroke="none"/><path d="M9.5 9V6.5h7V9" stroke-width="1.3"/><rect x="9.5" y="14" width="7" height="5" stroke-width="1.3"/></svg>
      <span>Email: hello@kestrelyield.com</span>
    </div>
    <div class="contact">
      <svg class="icon" viewBox="0 0 26 26" fill="none" stroke="currentColor" stroke-width="1.6"><circle cx="13" cy="13" r="11.5"/><rect x="7.5" y="8.5" width="11" height="7" stroke-width="1.4"/><path d="M10 19h6M13 15.5V19" stroke-width="1.4"/></svg>
      <span>Fax: 00 987654321</span>
    </div>
    <div class="contact">
      <svg class="icon" viewBox="0 0 26 26" fill="none" stroke="currentColor" stroke-width="1.6"><circle cx="13" cy="13" r="11.5"/><rect x="7.5" y="9" width="11" height="8" fill="currentColor" stroke="none"/><path d="M7.5 9l5.5 4.5L18.5 9" stroke="#fff" stroke-width="1.2"/></svg>
      <span>Web: www.kestrelyield.com</span>
    </div>
  </div>

  <div class="band">
    <svg class="icon" viewBox="0 0 26 26" fill="none" stroke="currentColor" stroke-width="1.6"><circle cx="13" cy="13" r="11.5"/><path d="M13 20s-4.5-5-4.5-8a4.5 4.5 0 0 1 9 0c0 3-4.5 8-4.5 8z"/><circle cx="13" cy="12" r="1.5"/></svg>
    <span>P.O.Box: 5678, Fenmoor Lane, Office No: 2040, Leeds, United Kingdom</span>
  </div>
</section>

<section class="card card--back" aria-label="Card back">
  <div class="brand">
    <span class="brand__dot"></span>
    <p class="brand__name"><span>Kestrel Yield</span><span>Consulting</span></p>
  </div>
  <div class="band">www.kestrelyield.com</div>
</section>

</body>
</html>
```